Website for Marlow Crest Telecom

I need a website done for Marlow Crest Telecom, a new telecommunications business launching in Australia which provides the best internet connectivity for Businesses. It needs to start with the home page, including the logo, layout, colour, font. The rest of the website will follow, around 12 pages.

Ideally the logo will be maximum two colours, with the words Marlow Crest Telecom being the logo rather than another symbol. The emphasis needs to be on the word Marlow. The design needs to be simple and minimal. I am not sure yet whether the designer will code the page or I will get someone else to do it.

The colours on the slide attached are not meant to be the colours to use, but the layout is close to what I envisage.

```html
<!DOCTYPE html>
<html lang="en">
<head>
<meta charset="utf-8">
<title>Marlow Crest Telecom – Home</title>
<link href="https://fonts.googleapis.com/css2?family=Poppins:wght@300;400;500;600;700&display=swap" rel="stylesheet">
<style>
:root{
  --red:#ee2b2b;
  --red-dark:#c8191f;
  --ink:#111111;
  --grey-bg:#f4f4f4;
  --line:#cfcfcf;
  --footer:#2a2a2a;
  --white:#ffffff;
}
*{box-sizing:border-box;margin:0;padding:0}
html,body{width:1200px;height:2857px;overflow:hidden}
body{font-family:'Poppins',sans-serif;color:var(--ink);position:relative;background:var(--white)}
.abs{position:absolute}
a{color:inherit;text-decoration:none}

.topbar{left:0;top:0;width:1200px;height:38px;background:var(--red);color:var(--white);font-size:15px;font-weight:600}
.topbar .item{position:absolute;top:9px;display:flex;align-items:center;gap:6px}
.topbar .dot{width:24px;height:24px;border-radius:50%;background:rgba(255,255,255,.9);display:inline-flex;align-items:center;justify-content:center}
.topbar .sep{position:absolute;top:4px;width:1px;height:30px;background:rgba(255,255,255,.6)}

.nav{left:0;top:38px;width:1200px;height:72px;background:var(--white)}
.brand{position:absolute;left:101px;top:19px;font-size:28px;line-height:34px;font-weight:300;color:#222;white-space:nowrap}
.brand b{color:var(--red);font-weight:600}
.menu{position:absolute;top:26px;font-size:15px;font-weight:500}
.menu.active{color:var(--red)}

.hero{left:0;top:110px;width:1200px;height:625px;background:linear-gradient(180deg,#1d3a63 0%,#2a3f6a 25%,#5b3a5c 40%,#2a2440 60%,#231a2c 80%,#3a2218 100%)}
.hero h1{position:absolute;left:104px;top:220px;font-size:38px;font-weight:700;color:var(--white);letter-spacing:.5px;white-space:nowrap}
.hero p{position:absolute;left:104px;top:280px;font-size:16px;font-weight:600;color:var(--white);line-height:30px}
.btn-red{position:absolute;background:var(--red);color:var(--white);font-weight:600;display:flex;align-items:center;justify-content:center;border-radius:2px}
.hero .arrow{position:absolute;top:290px}
.down{left:576px;top:711px;width:48px;height:48px;border-radius:50%;background:var(--white);box-shadow:0 2px 6px rgba(0,0,0,.15);display:flex;align-items:center;justify-content:center;z-index:5}

.benefits{left:0;top:735px;width:1200px;height:682px;background:var(--grey-bg)}
.benefits h2{position:absolute;width:1200px;top:72px;text-align:center;font-size:44px;font-weight:400}
.benefits h2 b{color:var(--red);font-weight:700}
.benefit{position:absolute;font-size:14px;line-height:20px;color:#222}
.benefit h3{font-size:20px;font-weight:600;line-height:26px;color:var(--ink)}
.benefit.left{text-align:right}

.check{left:0;top:1417px;width:1200px;height:524px;background:var(--white)}
.check h2{position:absolute;left:100px;top:68px;width:520px;font-size:26px;line-height:33px;font-weight:400}
.check h2 b{font-weight:600}
.check label{position:absolute;left:104px;top:179px;font-size:16px}
.field{position:absolute;height:44px;border:1px solid #c9c9c9;font-size:13px;color:#444;padding:13px 10px}
.photo-frame{position:absolute;border:2px solid var(--red)}

.cta{left:0;top:1941px;width:1200px;height:493px;background:radial-gradient(circle at 70% 40%,#f2403c 0%,#e52a2a 55%,#d51f22 100%)}
.cta h2{position:absolute;left:648px;top:145px;font-size:36px;font-weight:400;color:var(--white)}
.cta h2 b{font-weight:700}
.cta p{position:absolute;left:649px;top:200px;font-size:22px;line-height:34px;font-weight:500;color:var(--white)}
.btn-outline{position:absolute;left:647px;top:296px;width:172px;height:49px;border:2px solid var(--white);color:var(--white);font-size:15px;font-weight:600;display:flex;align-items:center;justify-content:center;border-radius:2px}

.footer{left:0;top:2434px;width:1200px;height:423px;background:var(--footer);color:var(--white)}
.footer .logo{position:absolute;left:101px;top:96px;line-height:38px;text-align:center;font-size:31px;font-weight:300}
.footer .logo b{font-weight:600;font-size:36px}
.social{position:absolute;top:193px;width:42px;height:42px;border-radius:50%;border:2px solid var(--white);display:flex;align-items:center;justify-content:center}
.col-sep{position:absolute;top:83px;width:1px;height:217px;background:#666}
.col-sep::before{content:"";position:absolute;left:-1px;top:0;width:3px;height:34px;background:#8a8aa8}
.col{position:absolute;top:86px;font-size:14px}
.col h4{font-size:17px;font-weight:600;margin-bottom:18px}
.col li{list-style:none;height:33px}
.contact li{display:flex;gap:6px;align-items:flex-start;line-height:18px;margin-bottom:0}
.rule{position:absolute;left:101px;top:358px;width:998px;height:1px;background:#555}
.legal{position:absolute;top:381px;font-size:14px}
</style>
</head>
<body>

<header class="abs topbar">
  <div class="item" style="left:356px"><span class="dot"><svg width="14" height="14" viewBox="0 0 24 24"><path d="M6 3l4 4-2 3c1 3 3 5 6 6l3-2 4 4-3 3C10 21 3 14 3 6z" fill="#ee2b2b"/></svg></span>1300 XXX XXX</div>
  <span class="sep" style="left:506px"></span>
  <div class="item" style="left:523px"><span class="dot"><svg width="14" height="14" viewBox="0 0 24 24"><rect x="3" y="6" width="18" height="12" fill="none" stroke="#ee2b2b" stroke-width="2"/><path d="M3 6l9 7 9-7" fill="none" stroke="#ee2b2b" stroke-width="2"/></svg></span>sales@marlowcrest.com.au</div>
  <span class="sep" style="left:800px"></span>
  <div class="item" style="left:818px"><span class="dot"><svg width="14" height="14" viewBox="0 0 24 24"><rect x="3" y="6" width="18" height="12" fill="none" stroke="#ee2b2b" stroke-width="2"/><path d="M3 6l9 7 9-7" fill="none" stroke="#ee2b2b" stroke-width="2"/></svg></span>support@marlowcrest.com.au</div>
</header>

<nav class="abs nav">
  <div class="brand"><b>MARLOW</b> Crest Telecom</div>
  <a class="menu active" style="left:498px">Home</a>
  <a class="menu" style="left:588px">Products</a>
  <a class="menu" style="left:701px">About</a>
  <a class="menu" style="left:791px">News &amp; Insights</a>
  <a class="menu" style="left:948px">Partners</a>
  <a class="menu" style="left:1038px">Contact</a>
</nav>

<section class="abs hero" role="img" aria-label="Night city skyline with glowing data light trails rising from the buildings">
  <svg class="arrow" style="left:58px" width="26" height="46" viewBox="0 0 26 46"><path d="M24 2L3 23l21 21" fill="none" stroke="#fff" stroke-width="2"/></svg>
  <svg class="arrow" style="left:1114px" width="26" height="46" viewBox="0 0 26 46"><path d="M2 2l21 21L2 44" fill="none" stroke="#fff" stroke-width="2"/></svg>
  <h1>MARLOW CREST TELECOM</h1>
  <p>Sed ut perspiciatis unde omnis iste natus error sit<br>voluptatem accusantium doloremque</p>
  <a class="btn-red" style="left:105px;top:361px;width:173px;height:50px;font-size:16px">GET STARTED</a>
</section>

<section class="abs benefits">
  <h2><b>OUR</b> Benefits</h2>
  <svg class="abs" style="left:0;top:0" width="1200" height="682" viewBox="0 0 1200 682">
    <g stroke="var(--line)" stroke-width="1.5" fill="none">
      <path d="M471 218L416 328L393 392L416 455L471 571"/>
      <path d="M729 218L785 328L807 392L790 455L729 571"/>
    </g>
    <polygon points="441,396 519,261 679,261 759,396 679,535 519,535" fill="#fff" stroke="#555" stroke-width="1.5"/>
    <defs><linearGradient id="core" x1="0" y1="0" x2="1" y2="1"><stop offset="0" stop-color="#e9323a"/><stop offset="1" stop-color="#8f1c24"/></linearGradient></defs>
    <polygon points="458,396 531,274 667,274 741,396 667,521 531,521" fill="url(#core)"/>
    <text x="599" y="392" text-anchor="middle" fill="#fff" font-family="Poppins,sans-serif" font-size="36" font-weight="600">MARLOW</text>
    <text x="600" y="430" text-anchor="middle" fill="#fff" font-family="Poppins,sans-serif" font-size="29" font-weight="300">Crest Telecom</text>
    <g fill="#fff" stroke="#bdbdbd" stroke-width="1.2">
      <polygon transform="translate(429,182)" points="0,36 21,0 63,0 84,36 63,72 21,72"/>
      <polygon transform="translate(374,292)" points="0,36 21,0 63,0 84,36 63,72 21,72"/>
      <polygon transform="translate(374,419)" points="0,36 21,0 63,0 84,36 63,72 21,72"/>
      <polygon transform="translate(429,535)" points="0,36 21,0 63,0 84,36 63,72 21,72"/>
      <polygon transform="translate(687,182)" points="0,36 21,0 63,0 84,36 63,72 21,72"/>
      <polygon transform="translate(743,292)" points="0,36 21,0 63,0 84,36 63,72 21,72"/>
      <polygon transform="translate(748,419)" points="0,36 21,0 63,0 84,36 63,72 21,72"/>
      <polygon transform="translate(687,535)" points="0,36 21,0 63,0 84,36 63,72 21,72"/>
    </g>
    <g fill="none" stroke="var(--red)" stroke-width="1.6" stroke-linecap="round">
      <path d="M455 226a16 16 0 0 1 32 0M471 226l8-9"/><circle cx="471" cy="226" r="3"/>
      <path d="M410 342v-24l6-8 6 8v24zM410 330h12"/>
      <rect x="402" y="447" width="28" height="20" rx="2"/><path d="M410 447v-4h12v4M402 456h28"/>
      <path d="M458 563l8-6 10 2 6 6 -2 10 -8 6 -10-2 -4-8z"/><circle cx="478" cy="580" r="3"/>
      <path d="M715 222l8-8 6 6 8-8M717 230h24"/>
      <circle cx="785" cy="324" r="11"/><path d="M774 324v6M796 324v6M785 341h6"/>
      <rect x="779" y="442" width="20" height="26" rx="1"/><path d="M783 450h12M783 456h12M783 462h8"/>
      <circle cx="729" cy="566" r="10"/><path d="M729 560v12M715 584h28"/>
    </g>
  </svg>
  <div class="benefit left" style="right:782px;top:182px"><h3>FAST</h3>From 100Mbps up to 1Gbps* speed<br>options</div>
  <div class="benefit left" style="right:838px;top:293px"><h3>DEDICATED fibre</h3>doesn’t slow down with multiple<br>concurrent users</div>
  <div class="benefit left" style="right:838px;top:420px"><h3>SYMMETRIC</h3>same download and upload speeds,<br>critical for business use</div>
  <div class="benefit left" style="right:782px;top:536px"><h3>WIDELY AVAILABLE</h3>to 1.5M sites around Australia including metro,<br>regional and remote locations</div>
  <div class="benefit" style="left:782px;top:182px"><h3>RELIABLE</h3>Designed for up to 99.95% network<br>availability with 4G back up option</div>
  <div class="benefit" style="left:833px;top:293px"><h3>EXPERT SUPPORT</h3>100% Australian team with 24x7<br>service</div>
  <div class="benefit" style="left:837px;top:420px"><h3>NO UPFRONT BUILD COST</h3>in 90% of cases on a standard 3 year<br>contract**</div>
  <div class="benefit" style="left:781px;top:549px"><h3>AFFORDABLE</h3>starting at $X per month</div>
</section>
<div class="abs down"><svg width="18" height="20" viewBox="0 0 18 20"><path d="M9 1v17M2 11l7 7 7-7" fill="none" stroke="#111" stroke-width="1.6"/></svg></div>

<section class="abs check">
  <h2><b>Find out if Corelink Enterprise<br>Ethernet is</b> available at your<br>business location.</h2>
  <label>Address</label>
  <div class="field" style="left:100px;top:212px;width:219px">Number</div>
  <div class="field" style="left:330px;top:212px;width:219px">Street</div>
  <div class="field" style="left:100px;top:266px;width:219px">Suburb</div>
  <div class="field" style="left:330px;top:266px;width:219px">State</div>
  <div class="field" style="left:100px;top:322px;width:450px">Postcode</div>
  <a class="btn-red" style="left:375px;top:380px;width:174px;height:50px;font-size:15px">SUBMIT</a>
  <div class="photo-frame" style="left:654px;top:64px;width:462px;height:367px"></div>
  <div class="abs" role="img" aria-label="Close-up of a fibre optic cable glowing orange with streams of binary data on a blue background" style="left:635px;top:81px;width:463px;height:367px;background:linear-gradient(90deg,#7a2a1a 0%,#e0561f 35%,#f7c27a 50%,#7fa5c8 75%,#2d5c8a 100%)"></div>
</section>

<section class="abs cta">
  <svg class="abs" style="left:142px;top:74px" width="400" height="347" viewBox="0 0 400 347" role="img" aria-label="Smiling customer support agent wearing a headset in a call centre">
    <polygon points="0,173 90,0 310,0 400,173 310,347 90,347" fill="#8d7a72"/>
  </svg>
  <h2><b>For more</b> information,</h2>
  <p>Call 1300 XXX XXX or<br>Email sales@marlowcrest.com.au</p>
  <a class="btn-outline">CONTACT US</a>
</section>

<footer class="abs footer">
  <div class="logo"><b>MARLOW</b><br>Crest Telecom</div>
  <a class="social" style="left:102px" aria-label="Social profile"><svg width="12" height="12"><circle cx="6" cy="6" r="3" fill="#fff"/></svg></a>
  <a class="social" style="left:155px" aria-label="Social profile"><svg width="12" height="12"><circle cx="6" cy="6" r="3" fill="#fff"/></svg></a>
  <a class="social" style="left:210px" aria-label="Social profile"><svg width="12" height="12"><circle cx="6" cy="6" r="3" fill="#fff"/></svg></a>
  <a class="social" style="left:263px" aria-label="Social profile"><svg width="12" height="12"><circle cx="6" cy="6" r="3" fill="#fff"/></svg></a>

  <span class="col-sep" style="left:364px"></span>
  <span class="col-sep" style="left:583px"></span>
  <span class="col-sep" style="left:780px"></span>

  <div class="col" style="left:421px"><h4>Quick Link</h4><ul><li>Home</li><li>&nbsp;Products</li><li>About</li><li>News &amp; Insights</li><li>Partners</li><li>Contact</li></ul></div>
  <div class="col" style="left:641px"><h4>Other Link</h4><ul><li>Who We Are</li><li>Career</li><li>News</li><li>Resources</li><li>Contact</li></ul></div>
  <div class="col contact" style="left:840px"><h4>Contact Info</h4><ul>
    <li style="height:57px"><svg width="14" height="16" viewBox="0 0 14 16"><path d="M7 15S1 9 1 6a6 6 0 0 1 12 0c0 3-6 9-6 9z" fill="#fff"/><circle cx="7" cy="6" r="2" fill="#2a2a2a"/></svg>1234 Somestreet&nbsp; Anywhere<br>USA 21212</li>
    <li style="height:40px"><svg width="16" height="16" viewBox="0 0 24 24"><path d="M6 3l4 4-2 3c1 3 3 5 6 6l3-2 4 4-3 3C10 21 3 14 3 6z" fill="#fff"/></svg>1300 XXX XXX</li>
    <li style="height:32px"><svg width="16" height="14" viewBox="0 0 24 18"><rect x="1" y="1" width="22" height="16" fill="#fff"/><path d="M1 1l11 9 11-9" fill="none" stroke="#2a2a2a" stroke-width="2"/></svg>sales@marlowcrest.com.au</li>
    <li><svg width="16" height="14" viewBox="0 0 24 18"><rect x="1" y="1" width="22" height="16" fill="#fff"/><path d="M1 1l11 9 11-9" fill="none" stroke="#2a2a2a" stroke-width="2"/></svg>support@marlowcrest.com.au</li>
  </ul></div>

  <div class="rule"></div>
  <div class="legal" style="left:101px">Copyright © 2022 -&nbsp; Marlow Crest Telecom. All Right Reserved</div>
  <div class="legal" style="right:101px">Privacy Policy&nbsp; |&nbsp; Terms &amp; Conditions</div>
</footer>

</body>
</html>
```